Onboarding Infographic/brochure

We are a small criminal defense firm looking to create some sort of infographic or brochure that we can onboard new clients with. We are currently sending it out via email but want something a bit cooler and fun to send to clients. The information is:

A Few Quick Rules

We are here to help each step of the way. While questions are never discouraged, this letter will answer some of the most common ones we get asked.

Communications

As a client, you should always be in the loop. While we will try to respond to questions as quickly as possible, sometimes we are unable to respond right away. Do not worry - we promise to get back to you soon. Some questions might take some time to research, and a correct answer is better than a quick one.

Appointments

One of the benefits of having an attorney is the ability to discuss your case outside of court, minus the stress and headaches. If you need an appointment, please contact the office.

Appointments must be scheduled in advance. We do not want you to make a special trip to the office only to learn that we are in court or otherwise unavailable.

Jail Visits

If your family member is currently in jail, we take that very seriously. We will visit your loved one and introduce ourselves. While the case is ongoing, we ask that a family member be designated a “contact” person so that messages can be relayed quickly. Never discuss the facts of the case over the phone with someone who is in jail. Jail calls are recorded and we have seen too many cases go south based on remarks made over recorded lines.

Police Reports and Discovery

We will do our best to provide you with copies of everything we receive on your case. Most information will be emailed, so please keep your email address up to date.

Changes in Contact Information

If you move or change numbers during the case, please let us know. It is difficult to help if we are unable to reach you, and helping you is why we are here.

Court Appearances

Cases do not get resolved as quickly as they do on television. Expect there to be several hearings in your case and it may be necessary for you to attend one or more of them. If a hearing is set, you will receive notice of the date and time of each hearing.

Billing and Collections

We understand that this investment was a huge decision for you. As we focus on providing the best representation, we will need for you to stay on schedule with any payment arrangements agreed to at the time of your initial consultation.

Again, thank you for your trust in us. We look forward to getting a fantastic outcome on your case.

Target Market(s)

Criminal defense clients and their families

Industry/Entity Type

Legal

Font styles to use
Serif

Requirements
Must have
• Must incorporate all of the rules we email out. Would like diagrams, images or pictures
Nice to have
• We attached a Welcome brochure. Not sure I want it to look super similar, hence the request for infographic.

```html
<!DOCTYPE html>
<html lang="en">
<head>
<meta charset="utf-8">
<title>A Few Quick Rules – Veritas Defense Group</title>
<link rel="stylesheet" href="https://fonts.googleapis.com/css2?family=Poppins:wght@400;500;600;700;800&display=swap">
<style>
:root{
  --page-bg:#ffffff;
  --navy:#1e3a66;
  --navy-deep:#172e55;
  --ink:#16213a;
  --body:#1d1d1f;
  --sky:#8eaee0;
  --orange:#e8a24a;
  --ring:#7d9fd8;
}
*{box-sizing:border-box;margin:0;padding:0}
html,body{width:1023px;height:1200px;overflow:hidden;background:var(--page-bg);font-family:"Poppins",sans-serif}
.sheet{position:absolute;left:71px;top:30px;width:880px;height:1140px;background:#fff}
.side{position:absolute;left:0;top:0;width:376px;height:100%;
  background:linear-gradient(180deg,#2c4c7d 0%,#22406f 45%,var(--navy-deep) 100%);color:#fff;text-align:center}
.brand{position:absolute;top:46px;left:0;width:100%}
.brand-name{font-weight:700;font-size:34px;letter-spacing:1px;line-height:1}
.brand-sub{font-weight:600;font-size:13px;letter-spacing:9px;margin-top:4px;padding-left:9px}
.title-small{position:absolute;top:150px;left:0;width:100%;font-weight:400;font-size:72px;line-height:1}
.title-big{position:absolute;top:232px;left:0;width:100%;font-weight:800;font-size:94px;line-height:92px;color:var(--sky);letter-spacing:-1px}
.tagline{position:absolute;top:434px;left:36px;width:304px;font-size:23.5px;line-height:31px}
.temple{position:absolute;left:50px;top:692px;width:292px;height:290px;border-radius:6px;
  background:linear-gradient(180deg,#e7ad5f 0%,#c98538 55%,#8a4f1c 100%)}
.url{position:absolute;top:1062px;left:0;width:100%;font-size:17px;letter-spacing:1.6px}
.rule{position:absolute}
.num{color:var(--orange);font-weight:600;font-size:28px;line-height:1;position:absolute}
.head{color:var(--ink);font-weight:700;font-size:15.5px;line-height:19px;position:absolute;letter-spacing:.2px}
.line{position:absolute;height:1px;background:var(--orange)}
.line::after{content:"";position:absolute;right:-3px;top:-2px;width:5px;height:5px;border-radius:50%;background:var(--orange)}
.txt{position:absolute;font-size:11.4px;line-height:13.9px;color:var(--body)}
.txt p+p{margin-top:4px}
.badge{position:absolute;width:130px;height:130px;border-radius:50%;border:3px solid var(--ring);background:#fff;
  box-shadow:0 6px 8px -4px rgba(0,0,0,.18);padding:5px}
.badge .art{width:100%;height:100%;border-radius:50%}
</style>
</head>
<body>
<div class="sheet">
  <aside class="side">
    <div class="brand">
      <div class="brand-name">VERITAS</div>
      <div class="brand-sub">DEFENSE GROUP</div>
    </div>
    <div class="title-small">A FEW</div>
    <div class="title-big">QUICK<br>RULES</div>
    <p class="tagline">We are here to help each step of the way. While questions are never discouraged, this letter will answer some of the most common ones we get asked.</p>
    <div class="temple" role="img" aria-label="Illustration of a golden classical courthouse with columns"></div>
    <div class="url">www.veritasdefensegroup.com</div>
  </aside>

  <!-- 01 -->
  <div class="num" style="left:404px;top:42px">01</div>
  <div class="head" style="left:436px;top:46px">COMMUNICATIONS</div>
  <div class="line" style="left:404px;top:68px;width:202px"></div>
  <div class="txt" style="left:404px;top:77px;width:280px">As a client, you should always be in the loop. While we will try to respond to questions as quickly as possible, sometimes we are unable to respond right away. Do not worry - we promise to get back to you soon. Some questions might take some time to research, and a correct answer is better than a quick one.</div>
  <div class="badge" style="left:687px;top:49px"><div class="art" role="img" aria-label="Illustration of a client meeting an attorney at a desk" style="background:linear-gradient(160deg,#f3e6cf,#d9b98a 60%,#2f5a8a)"></div></div>

  <!-- 02 -->
  <div class="badge" style="left:407px;top:197px"><div class="art" role="img" aria-label="Illustration of two people talking at a table with speech bubbles" style="background:linear-gradient(160deg,#ffffff,#eef1f6 55%,#b7c6dd)"></div></div>
  <div class="num" style="left:551px;top:205px">02</div>
  <div class="head" style="left:590px;top:208px">APPOINTMENTS</div>
  <div class="line" style="left:551px;top:229px;width:204px"></div>
  <div class="txt" style="left:554px;top:235px;width:280px"><p>One of the benefits of having an attorney is the ability to discuss your case outside of court, minus the stress and headaches. If you need an appointment, please contact the office.</p><p>Appointments must be scheduled in advance. We do not want you to make a special trip to the office only to learn that we are in court or otherwise unavailable.</p></div>

  <!-- 03 -->
  <div class="num" style="left:404px;top:363px">03</div>
  <div class="head" style="left:453px;top:364px">JAIL VISITS</div>
  <div class="line" style="left:404px;top:385px;width:205px"></div>
  <div class="txt" style="left:404px;top:393px;width:272px">If your family member is currently in jail, we take that very seriously. We will visit your loved one and introduce ourselves. While the case is ongoing, we ask that a family member be designated a “contact” person so that messages can be relayed quickly. Never discuss the facts of the case over the phone with someone who is in jail. Jail calls are recorded and we have seen too many cases go south based on remarks made over recorded lines.</div>
  <div class="badge" style="left:681px;top:386px"><div class="art" role="img" aria-label="Illustration of a jail cell with guards and an inmate" style="background:linear-gradient(160deg,#8a3c3c,#b46a5e 50%,#d9cfc6)"></div></div>

  <!-- 04 -->
  <div class="badge" style="left:405px;top:551px"><div class="art" role="img" aria-label="Illustration of an arrest warrant on a clipboard with a gavel and handcuffs" style="background:linear-gradient(160deg,#c89a76,#b07a55 60%,#8e5a3a)"></div></div>
  <div class="num" style="left:547px;top:576px">04</div>
  <div class="head" style="left:597px;top:556px">POLICE REPORTS<br>AND DISCOVERY</div>
  <div class="line" style="left:547px;top:598px;width:206px"></div>
  <div class="txt" style="left:554px;top:607px;width:276px">We will do our best to provide you with copies of everything we receive on your case. Most information will be emailed, so please keep your email address up to date.</div>

  <!-- 05 -->
  <div class="num" style="left:404px;top:723px">05</div>
  <div class="head" style="left:459px;top:703px">CHANGES IN CONTACT<br>INFORMATION</div>
  <div class="line" style="left:404px;top:745px;width:209px"></div>
  <div class="txt" style="left:404px;top:752px;width:270px">If you move or change numbers during the case, please let us know. It is difficult to help if we are unable to reach you, and helping you is why we are here.</div>
  <div class="badge" style="left:675px;top:681px"><div class="art" role="img" aria-label="Illustration of a person updating contact details on a phone and computer" style="background:linear-gradient(160deg,#ffffff,#e9eef7 55%,#f08a8a)"></div></div>

  <!-- 06 -->
  <div class="badge" style="left:405px;top:823px"><div class="art" role="img" aria-label="Illustration of a judge seated at the courtroom bench" style="background:linear-gradient(180deg,#ffffff 0%,#f3eee9 45%,#8d3a34 70%,#6e2a26)"></div></div>
  <div class="num" style="left:551px;top:835px">06</div>
  <div class="head" style="left:592px;top:836px">COURT APPEARANCES</div>
  <div class="line" style="left:551px;top:857px;width:237px"></div>
  <div class="txt" style="left:554px;top:863px;width:280px">Cases do not get resolved as quickly as they do on television. Expect there to be several hearings in your case and it may be necessary for you to attend one or more of them. If a hearing is set, you will receive notice of the date and time of each hearing.</div>

  <!-- 07 -->
  <div class="num" style="left:404px;top:973px">07</div>
  <div class="head" style="left:442px;top:973px">BILLING AND COLLECTIONS</div>
  <div class="line" style="left:404px;top:995px;width:275px"></div>
  <div class="txt" style="left:405px;top:1003px;width:250px">We understand that this investment was a huge decision for you. As we focus on providing the best representation, we will need for you to stay on schedule with any payment arrangements agreed to at the time of your initial consultation.</div>
  <div class="badge" style="left:693px;top:969px"><div class="art" role="img" aria-label="Illustration of online payment with money, coins and a piggy bank" style="background:linear-gradient(160deg,#f7b733,#f0a21c 60%,#2f6fb0)"></div></div>
</div>
</body>
</html>
```